Corvanta Business cards template

We're looking for something modern and elegant. We are a reseller of technology (computers, datacenter, etc). Color theme would be "only" white with the incorporation of the blue that's present on our website (Corvanta.com) and logo file. We would like for the card to provide all the necessary info for the specific person (Phone#, fax#, email, name, website URL) . I'm attaching the logo file to this request. Please have it show Ottawa/Chicago somewhere, without providing specific addresses.

Target Market(s)

All b2b

Industry/Entity Type

Business

Contact Information for Business Card

Please have the color scheme be represented by only the white and blue from our website (Corvanta.com) and logo. We would like to logo on the card, but not big and overwhelming. This card will be used as a template for anybody within the company, it should display the user's name, phone#, fax#, email, job title and website URL. Please have it show Ottawa/Chicago somewhere, without providing our specific addresses. Really, we're looking for a clean, simple and elegant look.

Font styles to use
Serif

Requirements
Must have
• Please see card details
Nice to have
• Please see card details
Should not have
• Anything tacky or tagline.

```html
<!DOCTYPE html>
<html lang="en">
<head>
<meta charset="utf-8">
<title>Corvanta Business Cards</title>
<link rel="stylesheet" href="https://fonts.googleapis.com/css2?family=Roboto:wght@400;500;700&display=swap">
<style>
  :root {
    --backdrop: #2a2a2a;
    --card-white: #f3f3f3;
    --brand-blue: #0b6fbd;
    --brand-blue-light: #2b93dc;
    --text-white: #ffffff;
    --text-soft: #e6f1fb;
  }
  html, body {
    margin: 0;
    padding: 0;
    width: 1200px;
    height: 960px;
    overflow: hidden;
    background: var(--backdrop);
    font-family: "Roboto", Arial, sans-serif;
  }
  .canvas {
    position: relative;
    width: 1200px;
    height: 960px;
  }
  .card {
    position: absolute;
    width: 600px;
    height: 341px;
    border-radius: 20px;
    overflow: hidden;
  }
  .card-front {
    left: 314px;
    top: 114px;
    background: var(--card-white);
  }
  .card-back {
    left: 311px;
    top: 472px;
    background: var(--brand-blue);
  }
  .front-wave {
    position: absolute;
    left: 0;
    top: 0;
    width: 600px;
    height: 341px;
  }
  .brand-name {
    position: absolute;
    margin: 0;
    font-weight: 500;
    letter-spacing: 0.5px;
    line-height: 1;
    white-space: nowrap;
  }
  .brand-name-front {
    left: 0;
    width: 600px;
    top: 68px;
    text-align: center;
    font-size: 46px;
    color: var(--brand-blue);
  }
  .person {
    position: absolute;
    left: 52px;
    top: 244px;
    color: var(--text-white);
  }
  .person-name {
    margin: 0;
    font-size: 20px;
    font-weight: 500;
    line-height: 1.1;
  }
  .person-title {
    margin: 4px 0 0;
    font-size: 15px;
    font-weight: 400;
  }
  .contact {
    position: absolute;
    left: 371px;
    top: 214px;
    color: var(--text-soft);
    font-size: 14.5px;
  }
  .contact-city {
    margin: 0 0 10px;
    font-size: 14.5px;
  }
  .contact-list {
    list-style: none;
    margin: 0;
    padding: 0;
  }
  .contact-list li {
    display: flex;
    align-items: center;
    gap: 7px;
    height: 19px;
  }
  .contact-icon {
    width: 13px;
    height: 13px;
    flex: none;
  }
  .back-pattern {
    position: absolute;
    inset: 0;
    background: linear-gradient(180deg, #0d73c2 0%, #0a6cb8 100%);
  }
  .brand-name-back {
    left: 0;
    width: 600px;
    top: 146px;
    text-align: center;
    font-size: 56px;
    color: var(--text-white);
  }
  .back-url {
    position: absolute;
    left: 0;
    width: 600px;
    top: 282px;
    margin: 0;
    text-align: center;
    font-size: 13px;
    letter-spacing: 4.5px;
    color: var(--text-soft);
  }
</style>
</head>
<body>
<main class="canvas">

  <section class="card card-front" aria-label="Card front">
    <svg class="front-wave" viewBox="0 0 600 341" aria-hidden="true">
      <path d="M0 155 C 80 190, 160 200, 300 190 C 420 182, 520 178, 600 200 L600 341 L0 341 Z" fill="#2b93dc"/>
      <path d="M0 172 C 90 200, 180 206, 310 196 C 430 188, 520 186, 600 206 L600 341 L0 341 Z" fill="#ffffff"/>
      <path d="M0 178 C 90 206, 180 210, 310 200 C 430 192, 520 190, 600 210 L600 341 L0 341 Z" fill="var(--brand-blue)"/>
    </svg>

    <p class="brand-name brand-name-front">Corvanta</p>

    <div class="person">
      <p class="person-name">DANIEL HART</p>
      <p class="person-title">CEO/FOUNDER</p>
    </div>

    <div class="contact">
      <p class="contact-city">Ottawa/Chicago</p>
      <ul class="contact-list">
        <li>
          <svg class="contact-icon" viewBox="0 0 16 16" aria-hidden="true"><path d="M3 1.5l3 .5 1 3.5-2 1.5c1 2 2.5 3.5 4.5 4.5l1.5-2 3.5 1 .5 3c-.5 1-1.5 1.5-2.5 1.5C7 15 1 9 1 4c0-1 .8-2 2-2.5z" fill="#fff"/></svg>
          <span>1-855-410-CORV (2678)</span>
        </li>
        <li>
          <svg class="contact-icon" viewBox="0 0 16 16" aria-hidden="true"><rect x="4" y="1" width="8" height="4" fill="#fff"/><rect x="1" y="5.5" width="14" height="6" rx="1" fill="#fff"/><rect x="4" y="10" width="8" height="5" fill="#fff" stroke="var(--brand-blue)" stroke-width="1"/></svg>
          <span>482 555 0173</span>
        </li>
        <li>
          <svg class="contact-icon" viewBox="0 0 16 16" aria-hidden="true"><rect x="1" y="3.5" width="14" height="9" fill="#fff"/><path d="M1 3.5l7 5 7-5" fill="none" stroke="var(--brand-blue)" stroke-width="1.2"/></svg>
          <span>info@corvanta.com</span>
        </li>
        <li>
          <svg class="contact-icon" viewBox="0 0 16 16" aria-hidden="true"><circle cx="8" cy="8" r="7" fill="#fff"/><path d="M5 4c2 1 1 3 3 3s1 3 3 4M9 2c0 2 2 2 3 1" fill="none" stroke="var(--brand-blue)" stroke-width="1.3"/></svg>
          <span>www.corvanta.com</span>
        </li>
      </ul>
    </div>
  </section>

  <section class="card card-back" aria-label="Card back">
    <div class="back-pattern" role="img" aria-label="Subtle repeating oval pattern in tonal blue"></div>
    <p class="brand-name brand-name-back">Corvanta</p>
    <p class="back-url">www.corvanta.com</p>
  </section>

</main>
</body>
</html>
```